Our new beauty salon requires a price list brochure

Our beauty clinic is a medical grade skin care clinic. So our salon is very clinical and professional in appearance. I would like the colours to be similar to our logo design with some nice texture or abstract shapes thrown in.
Pricelist, contact details and logo is attached
I would prefer it to be a 3 fold brochure.

Target Market(s)

Females aged 30-50

Colors
85acd3
cedeed
c4c4c4
5c5c5c
000000
ffffff
eea3c7
f9d9e8
dbdbdb

Requirements
Must have
• easy to read

```html
<!DOCTYPE html>
<html lang="en">
<head>
<meta charset="utf-8">
<title>Lumen Aesthetics – Brochure Cover</title>
<link rel="stylesheet" href="https://fonts.googleapis.com/css2?family=Raleway:ital,wght@0,300;0,400;1,300&display=swap">
<style>
  :root {
    --paper: #ffffff;
    --ink: #5c5c5c;
    --slate: #4f5d6b;
    --sky: #85acd3;
    --mist: #cedeed;
    --blush: #eea3c7;
  }
  html, body {
    margin: 0;
    padding: 0;
    width: 1200px;
    height: 2542px;
    overflow: hidden;
    background: var(--paper);
  }
  .cover {
    position: relative;
    width: 1200px;
    height: 2542px;
    background: var(--paper);
    font-family: "Raleway", sans-serif;
    color: var(--ink);
  }
  .brand {
    position: absolute;
    left: 0;
    top: 210px;
    width: 1200px;
    text-align: center;
    color: var(--slate);
    font-weight: 300;
  }
  .brand-name {
    display: block;
    font-size: 250px;
    line-height: 1;
    letter-spacing: 6px;
  }
  .brand-tag {
    display: block;
    margin-top: 70px;
    padding-left: 340px;
    font-size: 36px;
    letter-spacing: 24px;
  }
  .contact {
    position: absolute;
    right: 373px;
    top: 670px;
    text-align: right;
    font-weight: 300;
    font-size: 41px;
    line-height: 53px;
    margin: 0;
    font-style: normal;
  }
  .contact-web {
    margin-top: 10px;
    font-style: italic;
    font-size: 42px;
  }
  .contact-social {
    display: flex;
    justify-content: flex-end;
    align-items: center;
    gap: 14px;
    margin-top: 14px;
    font-size: 40px;
    color: #7a7a7a;
  }
  .social-mark {
    width: 50px;
    height: 50px;
    border-radius: 10px;
    background: var(--blush);
  }
  .social-mark--alt {
    background: var(--sky);
  }
  .botanical {
    position: absolute;
    left: 90px;
    top: 1170px;
    width: 740px;
    height: 1372px;
  }
</style>
</head>
<body>
  <main class="cover">
    <header class="brand">
      <span class="brand-name">lumen</span>
      <span class="brand-tag">AESTHETICS</span>
    </header>

    <address class="contact">
      <div>Lumen Aesthetics</div>
      <div>4/27 Harbour Road</div>
      <div>Seabrook Bay</div>
      <div>Western Australia</div>
      <div>(08) 9555 0142</div>
      <div class="contact-web">www.lumenaesthetics.com.au</div>
      <div class="contact-social"><span>lumen_aesthetics</span><span class="social-mark"></span></div>
      <div class="contact-social"><span>lumen aesthetics australia</span><span class="social-mark social-mark--alt"></span></div>
    </address>

    <svg class="botanical" viewBox="0 0 740 1372" role="img" aria-label="Pale blue silhouette of a delicate branching wildflower stem">
      <defs>
        <radialGradient id="botanical-wash" cx="0.6" cy="0.35" r="0.75">
          <stop offset="0" stop-color="#cedeed" stop-opacity="0.85"/>
          <stop offset="1" stop-color="#cedeed" stop-opacity="0"/>
        </radialGradient>
      </defs>
      <rect x="0" y="0" width="740" height="1372" fill="url(#botanical-wash)"/>
    </svg>
  </main>
</body>
</html>
```